HANDYMAN SERVICES

we provide a good,and reliable service.we do all aspects of home improvement ,also all garden services,and any repairs,no job too small,free quotes .
I am aiming towards the general public for clients,also be doing special rates for the elderly,and reducing the price for anyone who does a friend reference. It will be free quotes/consultation,all work will be guaranteed.
Now the type of work we do is cctv installation,decking,patio/driveway cleaning,garages for erecting/repairs,house/garage clearances,fit alarm systems,fit or repair windows/doors,lay patios,repair roofs,decorate interior/external,erect ariaels,lay driveways,erect or repair fencing,lay drainage,repair or erect guttering and soffits,water features,erect or repair kitchens/bathrooms,also plastering,lay lawns or repair,also repair/erect sheds.

```html
<!DOCTYPE html>
<html lang="en">
<head>
<meta charset="utf-8">
<title>Handyman Services Flyer</title>
<link href="https://fonts.googleapis.com/css2?family=Audiowide&family=Questrial&family=Satisfy&family=Oswald:wght@600&family=Courgette&display=swap" rel="stylesheet">
<style>
  :root {
    --page-bg: #0a4f95;
    --cream: #fdf6c8;
    --cream-light: #fffbe3;
    --red: #a50f12;
    --red-bright: #c8161b;
    --yellow: #ffd21a;
    --ink: #1b1b1b;
    --sep: #d4141b;
  }
  html, body {
    margin: 0;
    padding: 0;
    width: 1200px;
    height: 1020px;
    overflow: hidden;
    background: var(--page-bg);
  }
  .flyer {
    position: absolute;
    left: 107px;
    top: 97px;
    width: 997px;
    height: 703px;
    background: var(--cream);
    overflow: hidden;
  }
  .photo-tools {
    position: absolute;
    left: 0; top: 0;
    width: 385px; height: 285px;
    background: linear-gradient(135deg, #3f5f8c 0%, #5b6f8a 35%, #c99a55 60%, #e6dccb 100%);
  }
  .intro-panel {
    position: absolute;
    left: 385px; top: 0;
    width: 612px; height: 285px;
    background: linear-gradient(90deg, #f4e9c4 0%, var(--cream) 30%, var(--cream-light) 100%);
  }
  .title-banner {
    position: absolute;
    left: 0; top: 28px;
    width: 612px; height: 56px;
    background: var(--red);
    display: flex;
    align-items: center;
    justify-content: center;
  }
  .title-banner h1 {
    margin: 0;
    font-family: "Audiowide", sans-serif;
    font-weight: 400;
    font-size: 36px;
    color: var(--yellow);
    letter-spacing: 1px;
  }
  .intro-text {
    position: absolute;
    left: 0; top: 94px;
    width: 612px;
    margin: 0;
    text-align: center;
    font-family: "Satisfy", cursive;
    font-size: 29px;
    line-height: 42px;
    color: var(--ink);
    font-weight: 700;
  }
  .side-band {
    position: absolute;
    left: 0; top: 285px;
    width: 71px; height: 418px;
    background: linear-gradient(90deg, var(--red) 0%, #8e0c0f 100%);
  }
  .side-band span {
    position: absolute;
    left: 50%; top: 50%;
    transform: translate(-50%, -50%) rotate(-90deg);
    white-space: nowrap;
    font-family: "Questrial", sans-serif;
    font-size: 46px;
    letter-spacing: 2px;
    color: var(--yellow);
  }
  .services {
    position: absolute;
    left: 71px; top: 285px;
    width: 607px; height: 418px;
    background: var(--cream-light);
    margin: 0;
    padding: 14px 0 0;
    box-sizing: border-box;
    list-style: none;
    text-align: center;
    font-family: "Oswald", sans-serif;
    font-weight: 600;
    font-size: 21px;
    line-height: 43px;
    color: var(--ink);
    text-transform: uppercase;
  }
  .services .sep { color: var(--sep); padding: 0 3px; }
  .photo-drill {
    position: absolute;
    left: 678px; top: 285px;
    width: 319px; height: 418px;
    background: linear-gradient(160deg, #b9a48c 0%, #8e7b68 30%, #5e6f86 55%, #c9a882 80%, #d9c2a3 100%);
  }
  .quote-seal {
    position: absolute;
    left: 621px; top: 340px;
    width: 210px; height: 210px;
  }
  .quote-seal p {
    position: absolute;
    inset: 0;
    margin: 0;
    display: flex;
    flex-direction: column;
    align-items: center;
    justify-content: center;
    transform: rotate(-10deg);
    font-family: "Courgette", cursive;
    color: var(--yellow);
    font-size: 24px;
    line-height: 30px;
    text-align: center;
  }
</style>
</head>
<body>
  <main class="flyer">
    <div class="photo-tools" role="img" aria-label="Photo of a handyman with a cordless drill and a tool belt"></div>

    <section class="intro-panel">
      <div class="title-banner"><h1>HANDYMAN SERVICES</h1></div>
      <p class="intro-text">providing good and reliable service.<br>We do all aspects of home improvement,<br>also all garden services, and any repairs,<br>no job too small.</p>
    </section>

    <div class="side-band"><span>WHAT WE DO</span></div>

    <ul class="services">
      <li>CCTV Installation<span class="sep">|</span>Decking<span class="sep">|</span>Patio/Driveway Cleaning<span class="sep">|</span></li>
      <li>Garages for Erecting/Repairs<span class="sep">|</span>Fit Alarm Systems<span class="sep">|</span></li>
      <li>House/Garage Clearances<span class="sep">|</span>Lay Patios<span class="sep">|</span></li>
      <li>Fit or Repair Windows/Doors | Repair Roofs</li>
      <li>Decorate Interior/External<span class="sep">|</span>Erect Ariaels<span class="sep">|</span></li>
      <li>Lay Driveways<span class="sep">|</span>Erect or Repair Fencing<span class="sep">|</span>Lay Drainage<span class="sep">|</span></li>
      <li>Water Features<span class="sep">|</span>Repair or Erect Guttering and Soffits<span class="sep">|</span></li>
      <li>Erect or Repair Kitchens/Bathrooms<span class="sep">|</span>Also Plastering<span class="sep">|</span></li>
      <li>Lay Lawns or Repair<span class="sep">|</span>Also Repair/Erect Sheds.</li>
    </ul>

    <div class="photo-drill" role="img" aria-label="Photo of hands drilling into a wooden board"></div>

    <div class="quote-seal">
      <svg width="210" height="210" viewBox="0 0 210 210" aria-hidden="true">
        <circle cx="105" cy="105" r="97" fill="none" stroke="#a50f12" stroke-width="10" stroke-dasharray="3.5 3"/>
        <circle cx="105" cy="105" r="94" fill="#b31217"/>
        <circle cx="105" cy="105" r="84" fill="none" stroke="#ffd21a" stroke-width="1.5" stroke-dasharray="2 3"/>
      </svg>
      <p>For Free<br>Quotes Call<br>07700900418</p>
    </div>
  </main>
</body>
</html>
```